Maplerise Trading Inc. needs an innovative idea for letterhead and visiting cards.

Maplerise Trading Inc. is a Canadian brand since 2007. It is a renown dealer of kids and office furniture locally. Moreover, exporting electric fixtures e.g. switches, LED's, down-lights etc. to Middle East and Africa. We have initiated a number of steps including re-branding, to boost our export in 2020. We have successfully designed our new logo a few months ago through 'Artfolio' and now we are looking for an innovative idea for a letterhead.
Some key points:
• Red, black and white are the three colors used in all our packaging and furniture. (grey is optional)
• Shouldn’t be too wide.
• Use of watermark is preferable.
• You can visit our North American site at www.mapleriseinc.com. Export website of the company will be launched soon. www.mapleriseinc.ca
• Same letterhead will be used locally and internationally.
• Our new logo and sample packaging is attached.

```html
<!DOCTYPE html>
<html lang="en">
<head>
<meta charset="utf-8">
<title>Maplerise Trading Inc. – Letterhead</title>
<link href="https://fonts.googleapis.com/css2?family=Source+Sans+3:wght@400;500&display=swap" rel="stylesheet">
<style>
  :root {
    --brand-red: #8b1214;
    --ink-grey: #4d4d4f;
    --watermark-tint: #f0dfd8;
    --page-white: #ffffff;
    --page-edge: #333333;
    --backdrop: #ffffff;
  }
  html, body {
    margin: 0;
    padding: 0;
    width: 1200px;
    height: 1200px;
    overflow: hidden;
    background: var(--backdrop);
    font-family: "Source Sans 3", sans-serif;
  }
  .letterhead {
    position: absolute;
    left: 223px;
    top: 112px;
    width: 761px;
    height: 983px;
    box-sizing: border-box;
    background: var(--page-white);
    border: 1px solid var(--page-edge);
    box-shadow: 8px 10px 10px rgba(0, 0, 0, 0.28);
  }
  .brand {
    position: absolute;
    left: 62px;
    top: 33px;
    display: flex;
    align-items: center;
    gap: 14px;
  }
  .brand-square {
    width: 64px;
    height: 64px;
    border-radius: 6px;
    background: var(--brand-red);
  }
  .brand-name {
    font-weight: 500;
    font-size: 31px;
    line-height: 34px;
    letter-spacing: 2px;
    text-transform: uppercase;
    color: var(--brand-red);
  }
  .contact {
    position: absolute;
    left: 529px;
    top: 72px;
    font-weight: 500;
    font-size: 12px;
    line-height: 21px;
    color: var(--brand-red);
  }
  .contact p { margin: 0; }
  .watermark {
    position: absolute;
    left: 196px;
    top: 310px;
    width: 368px;
    height: 408px;
    display: flex;
    flex-direction: column;
    align-items: center;
    justify-content: center;
    gap: 28px;
  }
  .watermark-square {
    width: 150px;
    height: 150px;
    border-radius: 18px;
    background: var(--watermark-tint);
  }
  .watermark-name {
    font-weight: 500;
    font-size: 56px;
    line-height: 60px;
    letter-spacing: 3px;
    text-transform: uppercase;
    text-align: center;
    color: var(--watermark-tint);
  }
</style>
</head>
<body>
  <main class="letterhead">
    <header class="brand">
      <div class="brand-square"></div>
      <div class="brand-name">Maplerise<br>Trading</div>
    </header>

    <address class="contact" style="font-style: normal;">
      <p>Phone: +1 (888) 555-0142</p>
      <p>Email: info@mapleriseinc.com</p>
    </address>

    <div class="watermark" aria-hidden="true">
      <div class="watermark-square"></div>
      <div class="watermark-name">Maplerise<br>Trading</div>
    </div>
  </main>
</body>
</html>
```